Dentist Ad for Airline Magazine

A full page print ad for magazine. Details below.

Target Market(s)

Mine workers and rural patients who fly in and out of the main city.

Industry/Entity Type

Airline

Requirements
Must have
• Copywriting as per attachment. Magazine print specifications as per attachment. Inviting colours (blue shades, perhaps some green/yellow). Comforting look and picture. Professional feel. Picture can be of a smiling or sleeping relaxed person (see business websites http://www.calmharbordentalcare.com and http://www.willowbankdentalclinic.com.au) - as we bring patients with complex dental problems or fear of the dentist, back to health whilst they enjoy a relaxing sleep (sedation).
Nice to have
• - stylised image of an aeroplane route across the text or at the footer

```html
<!DOCTYPE html>
<html lang="en">
<head>
<meta charset="utf-8">
<title>Fly-in and Fly-out Dental Transformations</title>
<link href="https://fonts.googleapis.com/css2?family=Fira+Sans+Condensed:ital,wght@0,400;0,600;1,400;1,600&family=Roboto+Condensed:wght@400;700&family=Arimo:wght@400;700&display=swap" rel="stylesheet">
<style>
:root{
  --yellow:#f4e04a;
  --green:#8db52f;
  --green-dark:#7aa02a;
  --blue-text:#1783c4;
  --ink:#111;
  --red:#b3262c;
  --white:#fff;
}
*{margin:0;padding:0;box-sizing:border-box}
html,body{width:926px;height:1200px;overflow:hidden;background:#fff}
.ad{position:relative;width:926px;height:1200px;border:1px solid #222;background:#fff;font-family:"Arimo",Arial,sans-serif;color:var(--ink)}
.hero{position:absolute;left:19px;top:19px;width:887px;height:407px;
  background:linear-gradient(100deg,#1f8fd0 0%,#43b3e6 45%,#9bd9f3 70%,#dff3fb 100%)}
.hero-photo{position:absolute;right:0;top:0;width:468px;height:407px;
  background:radial-gradient(ellipse at 55% 45%,#e9c7a9 0%,#d8a886 35%,rgba(180,200,220,.6) 70%,rgba(223,243,251,0) 100%)}
.title-bar{position:absolute;left:18px;top:14px;width:578px;height:68px;border-radius:6px;
  background:linear-gradient(180deg,#2c3a48,#131d27);box-shadow:0 2px 4px rgba(0,0,0,.4)}
.title-bar h1{position:absolute;left:62px;top:13px;font-family:"Roboto Condensed",sans-serif;font-weight:700;font-size:33px;color:var(--yellow);letter-spacing:-.5px}
.title-bar svg{position:absolute;left:14px;top:14px}
.hero-copy{position:absolute;left:36px;top:150px;color:var(--white);font-family:"Fira Sans Condensed",sans-serif;font-style:italic}
.hero-copy .lead{font-weight:600;font-size:49px;line-height:58px}
.hero-copy .line{font-size:39px;line-height:56px}
.questions{position:absolute;left:39px;top:436px;display:flex;gap:8px}
.question{height:103px;border-radius:5px;background:linear-gradient(180deg,var(--green),var(--green-dark));
  color:var(--white);font-size:19px;line-height:21px;text-align:center;padding-top:6px;box-shadow:0 1px 2px rgba(0,0,0,.3)}
.intro{position:absolute;left:46px;top:549px;width:800px;font-size:19px;line-height:23.5px}
.intro em{color:var(--green);font-weight:700}
.lower{position:absolute;left:19px;top:662px;width:887px;height:517px;background:linear-gradient(180deg,#cfeaf7 0%,#eef8fc 40%,#fff 100%)}
.why{position:absolute;left:744px;top:618px;font-family:"Roboto Condensed",sans-serif;font-weight:700;font-size:29px;color:var(--blue-text)}
.panels{position:absolute;left:540px;top:646px;width:342px}
.panel{position:relative;height:128px;padding:14px 66px 0 15px;color:var(--white)}
.panel h3{font-weight:400;font-size:21px;line-height:22px;text-transform:uppercase;margin-bottom:8px}
.panel p{font-size:10.8px;line-height:14.6px}
.panel svg{position:absolute;right:16px;top:48px}
.panel:nth-child(1){background:#0f8fcd}
.panel:nth-child(2){background:#0ea3d8}
.panel:nth-child(3){background:#0bb3df}
.panel:nth-child(4){background:#07c4e6}
.pitch{position:absolute;left:46px;top:678px}
.pitch h2{font-family:"Roboto Condensed",sans-serif;font-weight:700;font-size:25px;color:var(--blue-text);line-height:28px}
.pitch .sub{font-family:"Roboto Condensed",sans-serif;font-size:25px;color:var(--blue-text);line-height:26px}
.smile-photo{position:absolute;left:390px;top:688px;width:82px;height:82px;background:linear-gradient(160deg,#c99a78,#f1e6dc)}
.brace{position:absolute;left:462px;top:669px}
.pitch-body{position:absolute;left:46px;top:764px;width:440px;font-size:18px;line-height:22.5px}
.call{position:absolute;left:48px;top:898px;font-size:17px}
.brand{position:absolute;left:48px;top:940px;display:flex;align-items:center;gap:10px;font-size:25px;color:#2d3a47}
.brand i{width:26px;height:26px;border-radius:50%;background:var(--blue-text);display:block}
.partner{position:absolute;left:352px;top:940px;display:flex;align-items:center;gap:10px;font-size:12px;line-height:13px;color:#2a5d8a;width:170px}
.partner i{width:30px;height:30px;border-radius:50%;background:#7da4c9;flex:none;display:block}
.contact{position:absolute;left:49px;top:998px;font-size:16.5px;line-height:22.5px}
.contact .num{font-weight:700}
.contact .web{color:var(--blue-text);font-weight:700;font-style:italic}
.roadside{position:absolute;left:446px;top:1030px;width:88px;height:92px;background:linear-gradient(180deg,#eef4f7 0%,#d9e5ec 60%,#b9c8d2 100%)}
.footer{position:absolute;left:48px;top:1133px;font-family:"Roboto Condensed",sans-serif;font-weight:700;font-size:20px;color:var(--red);display:flex;gap:8px}
.footer span+span{border-left:1px solid #777;padding-left:8px}
</style>
</head>
<body>
<div class="ad">
  <section class="hero">
    <div class="hero-photo" role="img" aria-label="Photo of a smiling mother and daughter cheek to cheek"></div>
    <div class="title-bar">
      <svg width="36" height="36" viewBox="0 0 36 36" aria-hidden="true"><path d="M18 0 L20 16 L36 18 L20 20 L18 36 L16 20 L0 18 L16 16Z" fill="#fff"/><circle cx="18" cy="18" r="5" fill="#fff"/></svg>
      <h1>Do you want a better looking smile?</h1>
    </div>
    <div class="hero-copy">
      <div class="lead">Fly-in and Fly-out</div>
      <div class="line">Dental Transformations</div>
      <div class="line">True Care, Advanced</div>
      <div class="line">Expertise, Minimal Visits</div>
    </div>
  </section>

  <div class="questions">
    <div class="question" style="width:146px">Embarassed<br>to Smile?</div>
    <div class="question" style="width:136px">Complex<br>dental<br>problems?</div>
    <div class="question" style="width:164px">Fear of the<br>dentist or just<br>can't find the<br>right one?</div>
    <div class="question" style="width:178px">No time for<br>endless<br>appointments?</div>
    <div class="question" style="width:198px">Wish you could<br>sleep your way to<br>a healthy and<br>attractive smile?</div>
  </div>

  <p class="intro"><em>If the answer is yes to any of these questions</em>, you are certainly not alone! In our<br>specialized Sleep Dentistry Centre, our renowned team provides gentle, compassionate,<br>advanced and extensive treatments often in the comfort of a<br>relaxing sleep (IV Sedation).</p>

  <div class="lower"></div>
  <div class="why">WHY US?</div>

  <div class="pitch">
    <h2>Sound too good to be true?</h2>
    <div class="sub">It's just what we do for our<br>patients every day.</div>
  </div>
  <div class="smile-photo" role="img" aria-label="Photo of a smiling man"></div>
  <svg class="brace" width="54" height="210" viewBox="0 0 54 210" aria-hidden="true"><path d="M6 4 C30 4 32 18 32 40 L32 80 C32 96 38 103 50 105 C38 107 32 114 32 130 L32 170 C32 192 30 206 6 206" fill="none" stroke="#1a8fd0" stroke-width="5"/></svg>
  <p class="pitch-body">Our patients come from all over<br>Western Australia to take advantage of this unique<br>and personalized service. We invite you to let us<br>care for you as well.</p>

  <div class="panels">
    <div class="panel"><h3>Comfortable<br>Surroundings</h3><p>We take the time to understand your needs so you can make the best decisions for your health. You are looked after by a friendly, highly qualified expert team in relaxed and comfortable surroundings.</p>
      <svg width="38" height="38" viewBox="0 0 38 38" aria-hidden="true"><circle cx="19" cy="19" r="18" fill="#fff"/><path d="M9 19 L28 10 L28 28Z" fill="#0d8ccb"/></svg></div>
    <div class="panel"><h3 style="margin-top:16px">Minimal Visits</h3><p>Our patients often have treatments that would normally take months completed in minimal visits - which is perfect for the Fly-in, Fly-out patient.</p>
      <svg width="38" height="38" viewBox="0 0 38 38" aria-hidden="true"><circle cx="19" cy="19" r="18" fill="#fff"/><path d="M9 19 L28 10 L28 28Z" fill="#0d8ccb"/></svg></div>
    <div class="panel"><h3 style="margin-top:14px">We Offer</h3><p>We offer a full range of dental treatments including dental implant surgeries and cosmetic rehabilitations all in-house.</p>
      <svg width="38" height="38" viewBox="0 0 38 38" aria-hidden="true"><circle cx="19" cy="19" r="18" fill="#fff"/><path d="M9 19 L28 10 L28 28Z" fill="#0d8ccb"/></svg></div>
    <div class="panel"><h3 style="margin-top:14px">Our Approach</h3><p>Our approach with Sleep Dentistry means Pain-Free, anxiety free, memory free procedures. Just excellent results and life changing treatments.</p>
      <svg width="38" height="38" viewBox="0 0 38 38" aria-hidden="true"><circle cx="19" cy="19" r="18" fill="#fff"/><path d="M9 19 L28 10 L28 28Z" fill="#0d8ccb"/></svg></div>
  </div>

  <div class="call">Call our friendly team today</div>
  <div class="brand"><i></i>willowbank dental</div>
  <div class="partner"><i></i><span>Calm Harbor Implant, Surgical &amp; Sedation Dentistry</span></div>

  <div class="contact">
    <div class="num">9400 5120 / 9400 5121</div>
    <div class="web">www.calmharbordentalcare.com</div>
    <div class="web">info@willowbankdentalclinic.com.au/</div>
    <div>info@calmharbordentalcare.com</div>
    <div>42 Harbour Lane Westvale WA 6010</div>
  </div>

  <div class="roadside" role="img" aria-label="Photo of an aeroplane road sign beside a road to the airport"></div>

  <div class="footer"><span>Fly-in</span><span>Fly-out</span><span>Dental Transformations</span><span>(08) 9400 5120</span></div>
</div>
</body>
</html>
```